Electronic hardware design and manufacturer needing a new business card design.

We need a new business card design consisting of a double sided design adhering to brand and logo guidelines attached. I also want to incorporate something that recognizes our 25th year in business ("EST 2001" or something like that....).

```html
<!DOCTYPE html>
<html lang="en">
<head>
<meta charset="utf-8">
<title>Northvale Circuit Works – Business Card</title>
<link href="https://fonts.googleapis.com/css2?family=Poppins:wght@400;500;600;700&display=swap" rel="stylesheet">
<style>
  :root {
    --bg: #2b2b2d;
    --navy: #0f2a3d;
    --navy-deep: #0b2233;
    --navy-tint: #163a52;
    --orange: #f5a21b;
    --orange-deep: #e8641e;
    --ink: #1d1d1f;
    --white: #ffffff;
    --rule: #b9b9b9;
  }
  * { box-sizing: border-box; margin: 0; padding: 0; }
  html, body { width: 1200px; height: 689px; overflow: hidden; }
  body {
    background: var(--bg);
    font-family: "Poppins", sans-serif;
    position: relative;
  }
  .card {
    position: absolute;
    top: 190px;
    width: 540px;
    height: 310px;
    border-radius: 22px;
    overflow: hidden;
  }
  /* Back side */
  .card-back { left: 30px; background: var(--navy); }
  .card-back .brand-mark {
    position: absolute; left: 0; right: 0; top: 118px;
    text-align: center;
    font-weight: 700; font-size: 34px; line-height: 1.1;
    color: var(--navy-tint);
    letter-spacing: 1px;
  }
  .card-back .brand-mark .tile {
    display: inline-block; width: 18px; height: 18px;
    background: var(--navy-tint); margin-right: 12px; vertical-align: 2px;
  }

  /* Front side */
  .card-front { left: 630px; background: var(--white); }
  .brand {
    position: absolute; left: 28px; top: 92px; width: 250px;
    font-weight: 700; font-size: 28px; line-height: 1.15;
    color: var(--navy);
  }
  .brand .tile {
    display: inline-block; width: 16px; height: 16px;
    background: var(--orange); margin-right: 8px; vertical-align: 2px;
  }
  .divider {
    position: absolute; left: 290px; top: 40px; width: 1px; height: 170px;
    background: linear-gradient(to bottom, transparent, var(--rule) 30%, var(--rule) 70%, transparent);
  }
  .details { position: absolute; left: 308px; top: 40px; width: 225px; color: var(--ink); }
  .details .person { font-weight: 700; font-size: 21px; color: var(--navy); line-height: 1.1; letter-spacing: .3px; }
  .details .role { font-weight: 500; font-size: 14px; color: var(--orange); margin-bottom: 12px; }
  .contact { list-style: none; font-size: 12px; line-height: 1.65; }
  .contact li { display: flex; align-items: center; gap: 7px; }
  .contact svg { width: 12px; height: 12px; flex: none; fill: var(--orange-deep); }
  .address { font-size: 12px; line-height: 1.4; margin-top: 10px; padding-left: 19px; }

  .band { position: absolute; left: 0; bottom: 0; width: 540px; height: 110px; }
  .anniversary {
    position: absolute; left: 180px; bottom: 20px;
    display: flex; align-items: flex-end; gap: 8px;
    color: var(--white); font-weight: 600; font-size: 12px; letter-spacing: 1px;
  }
  .anniversary .years { color: var(--orange); font-weight: 700; font-size: 40px; line-height: .9; }
  .anniversary .years sup { font-size: 13px; font-weight: 600; vertical-align: 22px; }
</style>
</head>
<body>

  <section class="card card-back" aria-label="Card back">
    <div class="brand-mark"><span class="tile"></span>Northvale<br>Circuit Works</div>
  </section>

  <section class="card card-front" aria-label="Card front">
    <div class="brand"><span class="tile"></span>Northvale<br>Circuit Works</div>
    <div class="divider"></div>

    <div class="details">
      <p class="person">DANIEL REYES</p>
      <p class="role">Managing Director</p>
      <ul class="contact">
        <li><svg viewBox="0 0 24 24"><path d="M6.6 10.8a15.1 15.1 0 0 0 6.6 6.6l2.2-2.2a1 1 0 0 1 1-.25 11.4 11.4 0 0 0 3.6.57 1 1 0 0 1 1 1V20a1 1 0 0 1-1 1A17 17 0 0 1 3 4a1 1 0 0 1 1-1h3.5a1 1 0 0 1 1 1c0 1.25.2 2.45.57 3.57a1 1 0 0 1-.25 1z"/></svg>044-555 010 220</li>
        <li><svg viewBox="0 0 24 24"><path d="M2 5h20v14H2zm2 2v.5l8 5 8-5V7l-8 5z"/></svg>hello@northvale.example</li>
        <li><svg viewBox="0 0 24 24"><path d="M12 2a10 10 0 1 0 0 20 10 10 0 0 0 0-20zm0 2c.9 1.2 1.6 2.6 2 4h-4c.4-1.4 1.1-2.8 2-4zM4.3 14a8 8 0 0 1 0-4h3.4a16 16 0 0 0 0 4zm.9 2h3a14 14 0 0 0 1.4 3.5A8 8 0 0 1 5.2 16zm3-8h-3a8 8 0 0 1 4.4-3.5A14 14 0 0 0 8.2 8zM12 20c-.9-1.2-1.6-2.6-2-4h4c-.4 1.4-1.1 2.8-2 4zm2.3-6H9.7a14 14 0 0 1 0-4h4.6a14 14 0 0 1 0 4zm.1 5.5a14 14 0 0 0 1.4-3.5h3a8 8 0 0 1-4.4 3.5zM16.3 14a16 16 0 0 0 0-4h3.4a8 8 0 0 1 0 4zm-.5-6a14 14 0 0 0-1.4-3.5A8 8 0 0 1 18.8 8z"/></svg>www.northvale.example</li>
      </ul>
      <p class="address">18, Harbour Row, Unit 4<br>30218, Westland</p>
    </div>

    <svg class="band" viewBox="0 0 540 110" preserveAspectRatio="none" aria-hidden="true">
      <path d="M0 62 Q300 58 540 0 L540 110 L0 110 Z" fill="var(--navy-deep)"/>
      <path d="M0 60 Q300 56 540 -2" fill="none" stroke="var(--orange)" stroke-width="2.5"/>
    </svg>
    <div class="anniversary">
      <span>CELEBRATING</span>
      <span class="years">25<sup>th</sup></span>
      <span>YEAR</span>
    </div>
  </section>

</body>
</html>
```